依頼詳細
朝陽経済報を読むターゲットに対して
我々の広告を打ちます。

伝えたいことは「普通じゃダメなんです」
HPをご確認のうえ、ジムの印象などもご確認ください。
https://kx7fit.example/
記載項目
キャッチ:普通のおじさんでは、出世できない
リード:とはいえ、残念ながら日本は精神的に老化しやすい環境が揃っているそう。かっこよさは若い人の特権のように考えられ、『かっこよく歳を重ねる』という意識が少ない傾向にある。ぜひ、当ジムで「おじさん化対策」を実践して欲しい

黒地に白文字でのデザインを想定しております。
裏面に当社の情報をいれるため
引き付けて裏面をめくりたくなるようなA面のデザインを依頼させていただきます。
サイズ
A4
ページ数
片面
希望イメージ
シンプル 複雑
単色 カラフル
暗い 明るい
日常 高級
遊び心 厳粛
未来的 伝統的
女性的 男性的
希望する色
無彩色系
納品ファイル
• 高解像度JPG (.jpg)
• イラストレーター形式 (.ai)
補足説明
下記ロゴデータを画面どこかへ配置をお願いします。
我々で考えたデザイン案は下記になります。
これとは違うデザインをご提案いただきたいです。

「普通のおじさんでは出世できない」

提案いただいた中で、このキャッチを
「絶望」「恐怖」などで提案いただきましたが
「警告」として色味や主張をいただいた点が決め手となりました。
単色の差し色をも、新聞折り込みのチラシとしての相性も良く
弊社満場一致で可決となりました。

合計で60超の提案をいただきました。
皆様クリエイティブ溢れるアイディアをありがとうございました。

・キャッチコピーの受け取り方が想定と違う
・「おじさん」の中でもとらえられるイメージが違う

我々からの定義の中でも、
ご依頼方法を再考しないといけないなと考える学びもありました。
この度は皆様ご協力いただきありがとうございました!!

```html
<!DOCTYPE html>
<html lang="ja">
<head>
<meta charset="utf-8">
<title>普通のおじさんでは、出世できない | KX7フィット</title>
<link rel="stylesheet" href="https://fonts.googleapis.com/css2?family=Shippori+Mincho+B1:wght@500;800&family=Noto+Sans+JP:wght@500&display=swap">
<style>
  :root {
    --bg: #000000;
    --ink: #ffffff;
  }
  html, body {
    margin: 0;
    padding: 0;
    width: 846px;
    height: 1200px;
    overflow: hidden;
    background: var(--bg);
  }
  .flyer {
    position: relative;
    width: 846px;
    height: 1200px;
    background: var(--bg);
    color: var(--ink);
    font-family: "Shippori Mincho B1", serif;
  }
  .catch {
    position: absolute;
    left: 74px;
    top: 176px;
    margin: 0;
    font-weight: 800;
    font-size: 52px;
    line-height: 70px;
    letter-spacing: 0.03em;
    white-space: nowrap;
  }
  .lead {
    position: absolute;
    left: 74px;
    top: 432px;
    margin: 0;
    font-weight: 500;
    font-size: 36px;
    line-height: 52px;
    letter-spacing: 0.04em;
    white-space: nowrap;
  }
  .brand {
    position: absolute;
    left: 430px;
    top: 898px;
    display: flex;
    align-items: center;
    gap: 12px;
    white-space: nowrap;
  }
  .brand-mark { display: block; flex: none; }
  .brand-text { display: flex; flex-direction: column; }
  .brand-name {
    font-family: "Shippori Mincho B1", serif;
    font-weight: 500;
    font-size: 32px;
    line-height: 1.1;
    letter-spacing: 0.06em;
    white-space: nowrap;
  }
  .brand-tagline {
    font-family: "Noto Sans JP", sans-serif;
    font-weight: 500;
    font-size: 13px;
    letter-spacing: 0.08em;
    margin-top: 4px;
    white-space: nowrap;
  }
</style>
</head>
<body>
  <main class="flyer">
    <h1 class="catch">普通のおじさんでは、<br>出世できない</h1>
    <p class="lead">
      とはいえ、残念ながら日本は精神的に<br>
      老化しやすい環境が揃っているそう。<br>
      かっこよさは若い人の特権のように<br>
      考えられ、『かっこよく歳を重ねる』と<br>
      いう意識が少ない傾向にある。ぜひ、<br>
      当ジムで「おじさん化対策」を実践し<br>
      て欲しい
    </p>
    <div class="brand">
      <svg class="brand-mark" width="54" height="54" viewBox="0 0 54 54" aria-hidden="true">
        <circle cx="27" cy="27" r="24.5" fill="none" stroke="var(--ink)" stroke-width="3"/>
      </svg>
      <div class="brand-text">
        <span class="brand-name">KX7フィット</span>
        <span class="brand-tagline">Private training studio</span>
      </div>
    </div>
  </main>
</body>
</html>
```